Luxury free range egg pack for eggs with golden orange yolks

We are looking for a new faced egg pack for one of our brands called Meadow Crest which is free range eggs with golden yolks.
This will be for a more up market target audience.

Target Market(s)

Luxury egg purchase

Industry/Entity Type

Egg production

Font styles to use
Decorative
Script

Colors
F0912C
F2A743
F7CA91
FBE8D2
FDF5EE

Requirements
Must have
• Orange or gold colouring in place in the theme

```html
<!DOCTYPE html>
<html lang="en">
<head>
<meta charset="utf-8">
<title>Meadow Crest Golden Free Range Eggs – Pack Label</title>
<link rel="stylesheet" href="https://fonts.googleapis.com/css2?family=Montserrat:wght@500;600&family=Playfair+Display:wght@500;700&family=Pinyon+Script&display=swap">
<style>
  :root {
    --orange-deep: #E9781F;
    --orange: #F0912C;
    --gold: #F2A743;
    --apricot: #F7CA91;
    --cream: #FBE8D2;
    --paper: #FDF5EE;
    --white: #FFFFFF;
  }
  * { box-sizing: border-box; margin: 0; padding: 0; }
  html, body { width: 1200px; height: 1200px; overflow: hidden; }
  body {
    background: var(--paper);
    font-family: "Montserrat", sans-serif;
    color: var(--white);
    position: relative;
  }
  .pack-label {
    position: absolute;
    left: 100px;
    width: 1000px;
    background: linear-gradient(100deg, var(--orange-deep) 0%, var(--orange) 60%, var(--gold) 100%);
    overflow: hidden;
  }
  .lid-top { top: 190px; height: 400px; }
  .lid-front { top: 630px; height: 320px; }

  .hen-art {
    position: absolute;
    background: linear-gradient(160deg, var(--cream), var(--apricot));
    opacity: 0.85;
    border-radius: 48% 52% 40% 44%;
  }
  .leaf-pattern {
    position: absolute;
    right: 0; top: 0; bottom: 0;
    width: 180px;
    background: linear-gradient(90deg, rgba(251,232,210,0) 0%, rgba(251,232,210,0.35) 45%, rgba(247,202,145,0.45) 100%);
  }

  .count {
    position: absolute;
    font-family: "Playfair Display", serif;
    font-weight: 700;
    line-height: 1;
    letter-spacing: -4px;
  }
  .count-size {
    position: absolute;
    font-family: "Montserrat", sans-serif;
    font-weight: 600;
    letter-spacing: 2px;
    transform: rotate(-18deg);
  }

  .brand-line {
    position: absolute;
    font-weight: 600;
    letter-spacing: 3px;
    text-transform: uppercase;
  }
  .product-name {
    position: absolute;
    font-family: "Playfair Display", serif;
    font-weight: 500;
    letter-spacing: 8px;
    line-height: 1;
  }
  .product-type {
    position: absolute;
    font-family: "Pinyon Script", cursive;
    line-height: 1;
  }
  .tagline {
    position: absolute;
    font-weight: 600;
    letter-spacing: 2px;
    text-transform: uppercase;
  }
  .rule { position: absolute; height: 1.5px; background: var(--cream); }
  .meals {
    position: absolute;
    font-family: "Playfair Display", serif;
    font-size: 12px;
    letter-spacing: 2.6px;
    text-transform: uppercase;
    white-space: nowrap;
  }
  .grade {
    position: absolute;
    font-weight: 600;
    font-size: 15px;
    letter-spacing: 2px;
  }

  .badge-row { position: absolute; display: flex; gap: 22px; align-items: center; }
  .badge-flag { width: 64px; height: 38px; background: var(--cream); border-radius: 3px; }
  .badge-round { width: 62px; height: 62px; border-radius: 50%; background: var(--cream); }
  .badge-wide { width: 86px; height: 52px; border-radius: 8px; background: var(--cream); }

  .seal-badge {
    position: absolute;
    width: 100px;
    height: 100px;
    border-radius: 50%;
    background: var(--cream);
  }
</style>
</head>
<body>

  <section class="pack-label lid-top" aria-label="Top face of lid">
    <div class="hen-art" role="img" aria-label="Engraved illustration of a hen" style="left:40px; top:120px; width:110px; height:100px;"></div>
    <div class="count" style="left:160px; top:70px; font-size:150px;">10</div>
    <div class="count-size" style="left:205px; top:225px; font-size:20px;">LARGE</div>

    <div class="badge-row" style="left:45px; top:275px;">
      <div class="badge-flag"></div>
      <div class="badge-round"></div>
      <div class="badge-wide"></div>
    </div>

    <div class="brand-line" style="left:400px; top:50px; font-size:19px;">Meadow Crest</div>
    <div class="product-name" style="left:392px; top:80px; font-size:84px;">GOLDEN</div>
    <div class="product-type" style="left:430px; top:165px; font-size:46px;">Free Range Eggs</div>
    <div class="tagline" style="left:400px; top:232px; font-size:19px;">With a richly golden yolk</div>
    <div class="rule" style="left:400px; top:264px; width:382px;"></div>
    <div class="meals" style="left:400px; top:274px;">Breakfast · Brunch · Lunch · Tea · Dinner</div>
    <div class="rule" style="left:400px; top:296px; width:382px;"></div>
    <div class="grade" style="left:540px; top:310px;">CLASS A</div>

    <div class="leaf-pattern" role="img" aria-label="Decorative hand-drawn leaf pattern"></div>
  </section>

  <section class="pack-label lid-front" aria-label="Front face of lid">
    <div class="hen-art" role="img" aria-label="Engraved illustration of a hen" style="left:40px; top:110px; width:80px; height:90px;"></div>
    <div class="count" style="left:125px; top:70px; font-size:130px;">10</div>
    <div class="count-size" style="left:150px; top:205px; font-size:18px;">LARGE</div>

    <div class="seal-badge" style="left:305px; top:85px;"></div>

    <div class="brand-line" style="left:450px; top:50px; font-size:19px;">Meadow Crest</div>
    <div class="product-name" style="left:440px; top:80px; font-size:84px;">GOLDEN</div>
    <div class="product-type" style="left:490px; top:170px; font-size:46px;">Free Range Eggs</div>

    <div class="seal-badge" style="left:845px; top:65px;"></div>
  </section>

</body>
</html>
```